Young, dynamic furniture company requires leaflet design

We require a new leaflet for our modern furniture company which supplies furniture and appliances to the property and development market.
Bramblecourt Furniture has become one of the leading furniture & appliance suppliers to the property market withing London. With over 10 years experience, we have increased our business to supply not only Private Landlords and Managing Agents, but also Property Developers, Housing Associations and Local Councils.
We offer not only a complete range of furniture which includes beds, wardrobes, dining sets and sofas, but also a high quality, full delivery and assembly service to help you with all our furnishing needs.

Target Market(s)

Private Landlords, Developers, Letting & Managing Agents

Industry/Entity Type

Furniture Store

Font styles to use
Sans Serif

Colors
0255a3
3176b5
85abd2
cfdeed
eaf1f7

Requirements
Must have
• Contact details,
• Our services:
• FREE next day delivery within the M25
• Free furniture assembly
• Free key pick up & drop off
• Free furniture removal (on a like-for-like basis)
• All types of furniture supplied - from basic to luxury

```html
<!DOCTYPE html>
<html lang="en">
<head>
<meta charset="utf-8">
<title>Bramblecourt Furniture – Trade Furniture Solutions</title>
<link rel="stylesheet" href="https://fonts.googleapis.com/css2?family=Roboto+Condensed:wght@300&family=Lato:wght@300&family=Open+Sans:wght@300;400;600&display=swap">
<style>
  :root {
    --navy: #232b6b;
    --page: #f2f2f3;
    --mist: #e3e4e8;
    --grey-band: #a9abb1;
    --white: #ffffff;
    --ink: #1f2340;
    --blue-deep: #1f6aa8;
    --blue-soft: #7d9dcb;
    --plum: #7a4b94;
    --blue-bright: #1a87c0;
    --photo-light: #e9ecef;
    --photo-mid: #d8d2c2;
  }
  html, body {
    margin: 0;
    padding: 0;
    width: 926px;
    height: 1200px;
    overflow: hidden;
    background: var(--page);
  }
  .leaflet {
    position: relative;
    width: 926px;
    height: 1200px;
    overflow: hidden;
    background: var(--page);
  }
  .leaflet-backdrop {
    position: absolute;
    inset: 0;
  }
  .brand-mark {
    position: absolute;
    left: 60px;
    top: 420px;
    width: 120px;
    height: 120px;
    background: var(--blue-deep);
  }
  .brand-name {
    position: absolute;
    left: 52px;
    top: 588px;
    margin: 0;
    font-family: "Roboto Condensed", sans-serif;
    font-weight: 300;
    font-size: 38px;
    line-height: 1;
    color: var(--white);
    text-transform: uppercase;
    letter-spacing: 0.2px;
  }
  .brand-tagline {
    position: absolute;
    left: 78px;
    top: 637px;
    margin: 0;
    font-family: "Roboto Condensed", sans-serif;
    font-weight: 300;
    font-size: 21px;
    line-height: 1;
    color: var(--white);
    text-transform: uppercase;
  }
  .intro {
    position: absolute;
    left: 52px;
    top: 689px;
    width: 824px;
    font-family: "Lato", sans-serif;
    font-weight: 300;
    font-size: 17.6px;
    line-height: 22.4px;
    color: var(--white);
    text-align: justify;
  }
  .intro p { margin: 0; }
  .services {
    position: absolute;
    left: 0;
    top: 0;
    width: 926px;
    height: 1200px;
    pointer-events: none;
  }
  .service {
    position: absolute;
    top: 869px;
    width: 180px;
    height: 180px;
    margin-left: -90px;
    border-radius: 50%;
    box-sizing: border-box;
    border: 4px solid var(--white);
    display: flex;
    flex-direction: column;
    align-items: center;
    justify-content: center;
    font-family: "Open Sans", sans-serif;
    color: var(--white);
    text-align: center;
    text-transform: uppercase;
  }
  .service-free {
    font-weight: 400;
    font-size: 35px;
    line-height: 38px;
  }
  .service-detail {
    font-weight: 300;
    font-size: 24px;
    line-height: 32px;
    white-space: nowrap;
  }
  .service--delivery { left: 208px; background: var(--blue-deep); }
  .service--assembly { left: 384px; background: var(--blue-soft); }
  .service--removal  { left: 555px; background: var(--plum); }
  .service--keys     { left: 731px; background: var(--blue-bright); }
  .contact-phone {
    position: absolute;
    left: 0;
    top: 1075px;
    width: 926px;
    display: flex;
    justify-content: center;
    align-items: center;
    gap: 6px;
    font-family: "Open Sans", sans-serif;
    font-weight: 600;
    font-size: 37px;
    color: var(--navy);
  }
  .contact-phone svg { width: 46px; height: 46px; }
  .contact-web {
    position: absolute;
    left: 0;
    top: 1136px;
    width: 926px;
    text-align: center;
    font-family: "Open Sans", sans-serif;
    font-weight: 600;
    font-size: 31px;
    letter-spacing: 1px;
    color: var(--ink);
  }
</style>
</head>
<body>
<main class="leaflet">
  <svg class="leaflet-backdrop" width="926" height="1200" viewBox="0 0 926 1200" aria-hidden="false">
    <defs>
      <linearGradient id="room-tones" x1="0" y1="0" x2="0" y2="1">
        <stop offset="0" stop-color="#eef1f3"/>
        <stop offset="0.55" stop-color="#e2ddd0"/>
        <stop offset="1" stop-color="#b9c4c8"/>
      </linearGradient>
      <radialGradient id="circle-shadow" cx="0.5" cy="0.5" r="0.5">
        <stop offset="0" stop-color="#000" stop-opacity="0.28"/>
        <stop offset="1" stop-color="#000" stop-opacity="0"/>
      </radialGradient>
    </defs>
    <rect class="room-photo" x="0" y="0" width="926" height="560" fill="url(#room-tones)" role="img" aria-label="Photograph of a bright living room with a cream sofa, two armchairs, table lamps and a lime green tufted ottoman"/>
    <path class="photo-edge" d="M0 270 C 110 330, 260 350, 430 345 C 620 340, 800 420, 926 520 L 926 560 L 0 560 Z" fill="var(--mist)"/>
    <path class="navy-field" d="M0 323 C 120 355, 300 365, 470 362 C 650 360, 820 440, 926 518 L 926 1000 C 860 1030, 780 1040, 700 1040 L 0 1040 Z" fill="var(--navy)"/>
    <path class="grey-band" d="M0 862 C 140 860, 260 905, 330 965 L 330 1000 L 0 1000 Z" fill="var(--grey-band)"/>
    <path class="page-foot" d="M0 925 C 120 905, 250 930, 330 975 C 520 1010, 760 1010, 926 1000 L 926 1200 L 0 1200 Z" fill="var(--page)"/>
    <ellipse cx="470" cy="1058" rx="360" ry="22" fill="url(#circle-shadow)"/>
  </svg>

  <div class="brand-mark" aria-hidden="true"></div>
  <h1 class="brand-name">Bramblecourt Furniture</h1>
  <p class="brand-tagline">Trade Furniture Solutions</p>

  <div class="intro">
    <p>Bramblecourt Furniture has become one of the leading furniture &amp; appliance suppliers to the property market withing London. With over 10 years experience, we have increased our business to supply not only Private Landlords and Managing Agents, but also Property Developers, Housing Associations and Local Councils.</p>
    <p>We offer not only a complete range of furniture which includes beds, wardrobes, dining sets and sofas, but also a high quality, full delivery and assembly service to help you with all our furnishing needs.</p>
  </div>

  <ul class="services" style="list-style:none;margin:0;padding:0;">
    <li class="service service--delivery"><span class="service-free">Free</span><span class="service-detail">Next Day</span><span class="service-detail">Delivery</span></li>
    <li class="service service--assembly"><span class="service-free">Free</span><span class="service-detail">Furniture</span><span class="service-detail">Assembly</span></li>
    <li class="service service--removal"><span class="service-free">Free</span><span class="service-detail">Furniture</span><span class="service-detail">Removal</span></li>
    <li class="service service--keys"><span class="service-free">Free</span><span class="service-detail">Key Pck Up &amp;</span><span class="service-detail">Drop Off</span></li>
  </ul>

  <div class="contact-phone">
    <svg viewBox="0 0 48 48" aria-hidden="true">
      <path d="M14 8 L20 8 L22 17 L17 20 C 19 26, 23 30, 28 32 L31 27 L40 29 L40 35 C 40 38, 37 40, 34 40 C 20 38, 10 28, 8 14 C 8 11, 11 8, 14 8 Z" fill="var(--ink)"/>
      <path d="M27 6 A 15 15 0 0 1 42 21" stroke="var(--blue-bright)" stroke-width="2.5" fill="none"/>
      <path d="M27 12 A 9 9 0 0 1 36 21" stroke="var(--blue-bright)" stroke-width="2.5" fill="none"/>
    </svg>
    <span>Call us on 020 7946 0321</span>
  </div>
  <div class="contact-web">WWW.BRAMBLECOURT.CO.UK</div>
</main>
</body>
</html>
```